Power Point - I have 5 webinars and each webinar has around 80-90 slides.

I have 5 webinars and each webinar has around 80-90 slides. This project is for the first of the five webinars; if the design is successful, the designer will be used for the subsequent 4 webinars, possibly for an increased fee.
The first of the 5 is a free webinar, showcasing what I can offer, as a service. The other 4 are on specific topics and the viewers will pay for them.
The target market for all the webinars are parents, but specifically, professional mothers who have children 10 years and under. ‘Professional’ is a loose term; they may have worked before they had children, they may work, part-time or full time, now, they may want to start a new career or project (set up a photography business, or community project).
I will provide the images and the copy for the designer. I would love the designer to use their creativity, so long as I get to look at the work and agree it as we go along. Since there are 5 webinars, I am happy for the whole thing to be working progress, as in we hone ‘the fit’ as we go along. The main thing I would like, over the 80-90 images is for each of them to represent the message I would like to portray. I want to be supportive of parents, offering them genuine methods for parenting.
The website and the logo are being designed now and will be incorporated into the following 4 webinars.
Actually, most of the slides, for this first (of 5 webinars) have been designed (around 35 have already been designed, leaving 50 more to be designed); the designer was unable to complete the rest. The file I have attached is a sample of what is required.

```html
<!DOCTYPE html>
<html lang="en">
<head>
<meta charset="UTF-8">
<title>Cashier of the Year – Slide</title>
<link href="https://fonts.googleapis.com/css2?family=Titillium+Web:wght@400;700&display=swap" rel="stylesheet">
<style>
  :root {
    --photo-deep: #140b04;
    --photo-mid: #4a2c0e;
    --photo-warm: #a86e24;
    --photo-glow: #e0a84a;
    --band-yellow: rgba(214, 168, 12, 0.94);
    --text-ink: #2f2a1c;
  }

  html, body {
    margin: 0;
    padding: 0;
    width: 1200px;
    height: 900px;
    overflow: hidden;
    background: var(--photo-deep);
  }

  .slide {
    position: relative;
    width: 1200px;
    height: 900px;
    overflow: hidden;
    font-family: "Titillium Web", sans-serif;
  }

  .slide__photo {
    position: absolute;
    inset: 0;
    background:
      radial-gradient(ellipse 420px 520px at 900px 470px, var(--photo-glow) 0%, var(--photo-warm) 35%, rgba(74, 44, 14, 0.6) 70%, transparent 100%),
      radial-gradient(ellipse 300px 200px at 1100px 80px, rgba(168, 110, 36, 0.7) 0%, transparent 100%),
      radial-gradient(ellipse 260px 180px at 180px 800px, rgba(168, 110, 36, 0.45) 0%, transparent 100%),
      radial-gradient(ellipse 300px 220px at 120px 120px, rgba(74, 44, 14, 0.8) 0%, transparent 100%),
      linear-gradient(90deg, var(--photo-deep) 0%, var(--photo-mid) 45%, var(--photo-deep) 100%);
  }

  .slide__caption {
    position: absolute;
    left: 0;
    top: 237px;
    width: 466px;
    height: 329px;
    box-sizing: border-box;
    padding: 40px 0 0 50px;
    background: var(--band-yellow);
    color: var(--text-ink);
    font-size: 36px;
    font-weight: 400;
    line-height: 57px;
  }

  .slide__caption p {
    margin: 0;
  }

  .slide__caption strong {
    font-weight: 700;
  }
</style>
</head>
<body>
  <main class="slide">
    <div class="slide__photo" role="img" aria-label="Close-up photograph of an ornate antique brass cash register with rows of round keys, lit in warm golden light against a dark background"></div>
    <div class="slide__caption">
      <p>I was never<br>going to win the<br><strong>‘Cashier of the Year’</strong><br>award</p>
    </div>
  </main>
</body>
</html>
```